New Jar Label for Manuka Honey Company!

Hine Roa Honey, a Manuka Honey company from New Zealand is looking for a fresh & engaging label for our manuka honey jars.

Attached are some examples of label designs that we like, feel free to use the language/copy on these labels for inspiration/content/copy, but feel free to add your own creative spin if you have a great design idea!

LABEL DIMENSIONS: 1654mmx532mm

Label Must Include:
- MGO rating
- Made (or) Product of New Zealand
- Manuka Honey (can add extra text similar to attached examples)

Label Can Include:
- Badges: raw food, non gmo, bpa free, gluten free, halal etc
- anything you feel is appropriate

You can change the color of the logo(s) to Black, White, Silver or Gold.

Can you please include a mockup of your label design(s) on the supplied "Jar Mockup File". You can change the scene of the mockup if you like.

UPDATE:

Have decided on bee logo so please bo longer use the mountain logo for label mockups. Design(s) will need multiple color variations to represent the other MGO ratings, flavor combos and other honey types, other than manuka.

• Provide multiple designs for each honey type
Manuka Design
Spring Honey Design
MGO 100-1000 Design(s)
Wildflower Honey Design
Flavor Combo Honey Design

```html
<!DOCTYPE html>
<html lang="en">
<head>
<meta charset="utf-8">
<title>Hine Roa Honey – Manuka Jar Label</title>
<link rel="stylesheet" href="https://fonts.googleapis.com/css2?family=Raleway:wght@400;500;700;800&family=Montserrat:wght@700&family=Roboto+Condensed:wght@400;700&display=swap">
<style>
  :root {
    --page: #ffffff;
    --label-bg: #1f1f1f;
    --gold: #e9bd45;
    --white: #ffffff;
    --green: #2fb34a;
    --seal: #8a8a8a;
  }
  * { margin: 0; padding: 0; box-sizing: border-box; }
  html, body { width: 1200px; height: 876px; overflow: hidden; background: var(--page); }
  body { position: relative; font-family: "Raleway", sans-serif; color: var(--white); }

  .label {
    position: absolute; left: 20px; top: 305px; width: 1160px; height: 265px;
    background: var(--label-bg); overflow: hidden;
  }
  .abs { position: absolute; }

  /* Producer block */
  .origin { left: 23px; top: 5px; font-size: 16px; font-weight: 500; line-height: 1; white-space: nowrap; }
  .origin strong { font-weight: 700; }
  .producer { left: 23px; top: 22px; font-size: 12.3px; line-height: 12.6px; white-space: nowrap; }
  .ingredients { left: 23px; top: 73px; font-size: 11.5px; line-height: 12.6px; white-space: nowrap; }
  .ingredients b { font-size: 15px; font-weight: 700; }

  /* Nutrition panel */
  .nutrition { left: 22px; top: 103px; width: 211px; height: 133px; border: 1px solid var(--white); overflow: hidden; }
  .nutrition h3 { text-align: center; font-size: 12px; font-weight: 500; line-height: 14px; border-bottom: 1px solid var(--white); margin: 0 2px; height: 15px; }
  .nutrition .head, .nutrition .row { position: relative; font-size: 6.6px; line-height: 8.2px; white-space: nowrap; }
  .nutrition .head { height: 22px; padding-top: 3px; border-bottom: 1px solid rgba(255,255,255,.6); margin: 0 4px; }
  .nutrition .body { padding-top: 4px; }
  .nutrition span { position: absolute; top: 0; }
  .nutrition .head span { top: 3px; }
  .c1 { left: 8px; } .c2 { left: 103px; } .c3 { left: 161px; }
  .nutrition .head .c1 { left: 4px; } .nutrition .head .c2 { left: 99px; } .nutrition .head .c3 { left: 157px; }
  .row { height: 8.6px; }
  .i1 { padding-left: 8px; } .i2 { padding-left: 14px; }

  .batch { left: 240px; top: 116px; width: 136px; height: 44px; background: var(--white); color: #222; font-size: 7px; font-weight: 500; padding: 2px 10px; line-height: 20px; }

  /* Brand mark */
  .brandmark { left: 582px; top: 8px; width: 82px; height: 82px; border: 1.5px solid var(--gold); border-radius: 50%; display: flex; align-items: center; justify-content: center; text-align: center; color: var(--gold); font-size: 11px; font-weight: 500; line-height: 13px; }

  .artwork { left: 379px; top: 84px; width: 205px; height: 173px; border-radius: 45% 40% 50% 45%; background: radial-gradient(ellipse at 55% 40%, #5a5448 0%, #3a3835 45%, var(--label-bg) 75%); }

  /* Product title */
  .title { left: 534px; top: 111px; font-family: "Montserrat", sans-serif; font-weight: 700; font-size: 38px; color: var(--gold); letter-spacing: 1px; line-height: 1; white-space: nowrap; }
  .subtitle { left: 532px; top: 146px; font-size: 16.5px; font-weight: 400; line-height: 1; letter-spacing: .2px; white-space: nowrap; }
  .claims { left: 520px; top: 180px; font-size: 10.6px; color: var(--gold); line-height: 1; white-space: nowrap; }
  .seal { top: 204px; width: 26px; height: 26px; border-radius: 50%; background: var(--seal); }
  .seal-a { left: 631px; }
  .seal-b { left: 664px; }
  .mgo { left: 697px; top: 203px; font-family: "Roboto Condensed", sans-serif; font-weight: 700; font-size: 11px; line-height: 12.5px; }
  .netwt { left: 635px; top: 236px; font-family: "Roboto Condensed", sans-serif; font-size: 12.5px; line-height: 1; white-space: nowrap; }

  /* Free-from badges */
  .badges { left: 772px; top: 11px; width: 36px; }
  .badge { position: relative; height: 47px; text-align: center; }
  .badge svg { display: block; margin: 0 auto; }
  .badge small { display: block; font-size: 3.4px; font-weight: 700; letter-spacing: .1px; margin-top: 1px; text-transform: uppercase; white-space: nowrap; }

  /* Story */
  .welcome { left: 832px; top: 16px; font-size: 17px; font-weight: 800; color: var(--gold); line-height: 1; letter-spacing: .2px; white-space: nowrap; }
  .story { left: 832px; top: 38px; font-size: 13.8px; line-height: 15.6px; white-space: nowrap; }
  .visit { left: 832px; top: 148px; font-size: 13.5px; color: var(--gold); line-height: 16px; letter-spacing: .3px; white-space: nowrap; }
  .social { top: 203px; display: flex; align-items: center; gap: 5px; font-size: 11px; line-height: 12.5px; white-space: nowrap; }
  .social i { width: 22px; height: 22px; border-radius: 50%; background: var(--white); display: block; flex: none; }
  .social-a { left: 834px; } .social-b { left: 1003px; }
</style>
</head>
<body>
<section class="label" aria-label="Manuka honey jar label">

  <p class="abs origin">product of <strong>New Zealand</strong></p>
  <p class="abs producer">Marketed and distributed by<br>Kowhai Valley Traders Ltd<br>58 Harbour Rd, Nelson, New Zealand<br>Tel +64(0)3 555 0192</p>
  <p class="abs ingredients"><b>Ingredients:</b> 100% South Island, NZ honey, No added sugar<br>No artifical flavours, colours or preservatives Store below 20oC</p>

  <div class="abs nutrition">
    <h3>Nutrition Information</h3>
    <div class="head">
      <span class="c1">Servings per package: 13<br>Serving size: 8ml</span>
      <span class="c2">Ave Quantity<br>per serve</span>
      <span class="c3">Ave Quantity<br>per 100g</span>
    </div>
    <div class="body">
      <div class="row"><span class="c1">Energy</span><span class="c2">14kJ</span><span class="c3">14kJ</span></div>
      <div class="row"><span class="c1">Protein</span><span class="c2">0g</span><span class="c3">0g</span></div>
      <div class="row"><span class="c1">Fat total</span><span class="c2">0g</span><span class="c3">0g</span></div>
      <div class="row"><span class="c1 i1">-saturated</span><span class="c2">0g</span><span class="c3">0g</span></div>
      <div class="row"><span class="c1 i1">-trans</span><span class="c2">0g</span><span class="c3">0g</span></div>
      <div class="row"><span class="c1 i2">-polyunsaturated</span><span class="c2">0g</span><span class="c3">0g</span></div>
      <div class="row"><span class="c1 i2">-monounsaturated</span><span class="c2">0g</span><span class="c3">0g</span></div>
      <div class="row"><span class="c1">Carbohydrate</span><span class="c2">8.7g</span><span class="c3">87g</span></div>
      <div class="row"><span class="c1 i1">-Sugars</span><span class="c2">8.1g</span><span class="c3">81g</span></div>
      <div class="row"><span class="c1">Sodium</span><span class="c2">0.7mg</span><span class="c3">7mg</span></div>
    </div>
  </div>

  <div class="abs batch">BEST BEFORE<br>BATCH NO.</div>

  <div class="abs brandmark">Hine Roa<br>Honey</div>

  <div class="abs artwork" role="img" aria-label="Illustration of dark tropical leaves and golden palm fronds"></div>

  <h1 class="abs title">MANUKA</h1>
  <p class="abs subtitle">NEW ZEALAND HONEY</p>
  <p class="abs claims">RAW, WILD, HALAL &amp; UNPASTEURIZED</p>

  <span class="abs seal seal-a" role="img" aria-label="Grading certificate seal"></span>
  <span class="abs seal seal-b" role="img" aria-label="Non-GMO certificate seal"></span>
  <p class="abs mgo">MGO<br>514+</p>
  <p class="abs netwt">Net Wt. 8.8 oz (250g)</p>

  <div class="abs badges">
    <div class="badge">
      <svg width="36" height="36" viewBox="0 0 36 36" aria-hidden="true"><circle cx="18" cy="18" r="16.5" fill="var(--green)" stroke="var(--white)" stroke-width="2"/><circle cx="18" cy="18" r="12" fill="var(--white)"/><path d="M12 23c0-7 5-11 12-11-1 7-5 11-12 11z" fill="none" stroke="var(--green)" stroke-width="1.4"/></svg>
      <small>All Natural</small>
    </div>
    <div class="badge">
      <svg width="36" height="36" viewBox="0 0 36 36" aria-hidden="true"><circle cx="18" cy="18" r="16.5" fill="var(--green)" stroke="var(--white)" stroke-width="2"/><circle cx="18" cy="18" r="12" fill="var(--white)"/><path d="M12 17l5 5 8-9" fill="none" stroke="var(--green)" stroke-width="2.6"/></svg>
      <small>Vegan</small>
    </div>
    <div class="badge">
      <svg width="36" height="36" viewBox="0 0 36 36" aria-hidden="true"><circle cx="18" cy="18" r="16.5" fill="var(--green)" stroke="var(--white)" stroke-width="2"/><circle cx="18" cy="18" r="12" fill="none" stroke="var(--white)" stroke-width="1.6"/><path d="M13 25l10-14M16 17l3 1M15 20l3 1" stroke="var(--white)" stroke-width="1.4"/><path d="M10 10l16 16" stroke="var(--white)" stroke-width="1.8"/></svg>
      <small>Gluten Free</small>
    </div>
    <div class="badge">
      <svg width="36" height="36" viewBox="0 0 36 36" aria-hidden="true"><circle cx="18" cy="18" r="16.5" fill="var(--green)" stroke="var(--white)" stroke-width="2"/><circle cx="18" cy="18" r="12" fill="none" stroke="var(--white)" stroke-width="1.6"/><rect x="15" y="11" width="6" height="15" rx="1.5" fill="var(--white)"/><path d="M10 26l16-16" stroke="var(--white)" stroke-width="1.8"/></svg>
      <small>Lactose Free</small>
    </div>
    <div class="badge">
      <svg width="36" height="36" viewBox="0 0 36 36" aria-hidden="true"><circle cx="18" cy="18" r="16.5" fill="var(--green)" stroke="var(--white)" stroke-width="2"/><circle cx="18" cy="18" r="12" fill="none" stroke="var(--white)" stroke-width="1.6"/><circle cx="14" cy="22" r="2" fill="var(--white)"/><circle cx="18" cy="18" r="2" fill="var(--white)"/><circle cx="22" cy="14" r="2" fill="var(--white)"/><path d="M10 10l16 16" stroke="var(--white)" stroke-width="1.8"/></svg>
      <small>Soya Free</small>
    </div>
  </div>

  <h2 class="abs welcome">Welcome to a world of good</h2>
  <p class="abs story">Where bees and hives are nurtured and honey<br>is kept in its most natural state, Where you'll<br>benefit from the fitnestquality nutrition, traceble<br>toits orgin, pure to its core. Where focusand<br>passion do a world of good</p>
  <p class="abs visit">Step into our world at<br>xxxxxxxxxxxx.com</p>

  <div class="abs social social-a"><i></i><span>friendbook.nz/<br>xxxxxxxxxxxxxxxxxxxx</span></div>
  <div class="abs social social-b"><i></i><span>snapgram.nz/<br>xxxxxxxxxxxxxxxxxx</span></div>

</section>
</body>
</html>
```